Criminal Defense Lawyer needs business cards and stationary
Dunmore Law Office
Criminal Defense Lawyer needs business cards and stationary - Law
Creative Brief
Simple
Ray Dunmore
418 N Willowbend Ave Lincoln, IL 62871
ray@dunmorelawoffice.example
dunmorelawoffice.example
I would like a simple/modern design for the front side of my card. I am thinking simply my logo in white with a blue background (same blue as in my logo). Other background colors to be considered are black and gray. That said, please be creative, I am open to any cutting edge design as long as it is not busy.
On the reverse side I would like my contact information displayed to include: My Name (Ray Dunmore) Dunmore Law Office (optional depending on design of front of card) Phone: 217-555-0143 email: ray@dunmorelawoffice.example Website: DunmoreLawOffice.example I do not want my address included. I am looking to create a visually modern yet simple design that is not too busy for the eye.
tavrelk tavrelk
Update: I have decided to add an additional winner. I will pick two designs that include business card and stationary. Thanks for the submissions. Also, designers, I am launching a website design contest soon. Keep an eye out for that.
Mistake in Brief. Please use phone number 217-555-0176 when submitting designs. Thank you.

```html
<!DOCTYPE html>
<html lang="en">
<head>
<meta charset="utf-8">
<title>Dunmore Law Office — Business Cards</title>
<link rel="stylesheet" href="https://fonts.googleapis.com/css2?family=Montserrat:wght@400;600;700&family=Roboto:wght@300;400&display=swap">
<style>
  :root {
    --page-bg: #e9e7e4;
    --card-blue: #1f5f9c;
    --card-gray: #5a5a5c;
    --frame-line: rgba(255,255,255,0.55);
    --ink-white: #ffffff;
    --ink-soft: #e4e4e4;
  }
  * { margin: 0; padding: 0; box-sizing: border-box; }
  html, body {
    width: 1200px;
    height: 891px;
    overflow: hidden;
    background: var(--page-bg);
  }
  .canvas {
    position: relative;
    width: 1200px;
    height: 891px;
    display: flex;
    align-items: center;
    justify-content: center;
    gap: 48px;
  }
  .card {
    position: relative;
    width: 520px;
    height: 297px;
    box-shadow: 0 10px 28px rgba(0,0,0,0.18);
  }
  .card__frame {
    position: absolute;
    inset: 10px;
    border: 1px solid var(--frame-line);
  }
  .card--back { background: var(--card-gray); }
  .card--front { background: var(--card-blue); }

  .brand {
    display: flex;
    flex-direction: column;
    align-items: center;
    gap: 12px;
  }
  .brand__dot {
    width: 44px;
    height: 44px;
    border-radius: 50%;
    background: var(--ink-white);
  }
  .brand__name {
    font-family: "Montserrat", sans-serif;
    font-weight: 700;
    font-size: 22px;
    letter-spacing: 3px;
    color: var(--ink-white);
    text-transform: uppercase;
  }

  .card--front .brand {
    position: absolute;
    left: 50%;
    top: 50%;
    transform: translate(-50%, -50%);
  }

  .card--back .brand {
    position: absolute;
    left: 40px;
    top: 48px;
  }
  .card--back .brand__dot { width: 36px; height: 36px; }
  .card--back .brand__name { font-size: 17px; letter-spacing: 2px; }

  .contact {
    position: absolute;
    left: 250px;
    top: 120px;
    font-family: "Roboto", sans-serif;
    color: var(--ink-soft);
  }
  .contact__name {
    font-family: "Montserrat", sans-serif;
    font-weight: 600;
    font-size: 17px;
    letter-spacing: 1px;
    color: var(--ink-white);
    text-transform: uppercase;
  }
  .contact__office {
    font-size: 13px;
    font-weight: 300;
    margin-top: 3px;
  }
  .contact__lines {
    list-style: none;
    margin-top: 18px;
    font-size: 13px;
    font-weight: 300;
    line-height: 1.55;
  }
</style>
</head>
<body>
<main class="canvas">
  <section class="card card--back" aria-label="Card reverse with contact details">
    <div class="card__frame"></div>
    <div class="brand">
      <span class="brand__dot"></span>
      <span class="brand__name">Dunmore</span>
    </div>
    <div class="contact">
      <p class="contact__name">Ray Dunmore</p>
      <p class="contact__office">Dunmore Law Office</p>
      <ul class="contact__lines">
        <li>217-555-0143</li>
        <li>ray@dunmorelawoffice.example</li>
        <li>DunmoreLawOffice.example</li>
      </ul>
    </div>
  </section>

  <section class="card card--front" aria-label="Card front with brand name">
    <div class="card__frame"></div>
    <div class="brand">
      <span class="brand__dot"></span>
      <span class="brand__name">Dunmore</span>
    </div>
  </section>
</main>
</body>
</html>
```